Hydraulics Company Business Card Design

Modern business card design for a hydraulics company.
Our company colours are - black, orange and white.
I would like the following contact details included-
Name
Position
Phone number
Email
Website
Street Address

I have attached our company logo.
I would like the back of the card white.

Thank you.

```html
<!DOCTYPE html>
<html lang="en">
<head>
<meta charset="UTF-8">
<title>Corvale Hydraulics – Business Card</title>
<link rel="stylesheet" href="https://fonts.googleapis.com/css2?family=Montserrat:wght@700;800&family=Poppins:wght@400;600;700&display=swap">
<style>
  :root {
    --navy: #0b1a2b;
    --orange: #f7931e;
    --orange-deep: #ff8a00;
    --white: #ffffff;
    --mist: #eeeeee;
    --ink: #1c2430;
    --rule: #d6d6d6;
    --page: #ffffff;
  }
  * { margin: 0; padding: 0; box-sizing: border-box; }
  html, body {
    width: 976px; height: 1200px; overflow: hidden;
    background: var(--page);
  }
  .canvas { position: relative; width: 976px; height: 1200px; }
  .card {
    position: absolute; left: 113px; width: 750px; height: 428px;
    border-radius: 44px; overflow: hidden; background: var(--white);
    border: 1px solid #ececec;
  }
  .card--front { top: 128px; }
  .card--back { top: 632px; }
  .card__art { position: absolute; inset: 0; width: 100%; height: 100%; }

  .brand {
    position: absolute; font-family: "Montserrat", sans-serif; font-weight: 800;
    color: var(--orange); line-height: 1;
  }
  .brand__main { display: block; }
  .brand__sub { display: block; letter-spacing: 0.06em; text-align: right; }

  .card--front .brand { left: 185px; top: 178px; }
  .card--front .brand__main { font-size: 60px; letter-spacing: -0.01em; }
  .card--front .brand__sub { font-size: 34px; margin-top: 8px; }

  .card--back .brand { left: 45px; top: 88px; }
  .card--back .brand__main { font-size: 34px; }
  .card--back .brand__sub { font-size: 19px; margin-top: 6px; }

  .person {
    position: absolute; right: 50px; top: 76px; text-align: right;
    font-family: "Poppins", sans-serif; color: var(--ink);
  }
  .person__name { font-size: 30px; font-weight: 700; letter-spacing: 0.01em; line-height: 1.1; }
  .person__role { font-size: 16px; font-weight: 400; margin-top: 4px; }

  .contacts {
    position: absolute; left: 350px; top: 210px; width: 310px;
    list-style: none; font-family: "Poppins", sans-serif; color: var(--ink);
  }
  .contacts__item {
    display: flex; justify-content: flex-end; align-items: center; gap: 18px;
    height: 47px; font-size: 19px; white-space: nowrap;
    border-bottom: 1.5px solid var(--rule);
    margin-left: 60px;
  }
  .contacts__item:last-child { border-bottom: none; margin-left: 0; }
  .contacts__icon { width: 18px; height: 18px; flex: none; }
</style>
</head>
<body>
<main class="canvas">

  <!-- Front of card -->
  <section class="card card--front" aria-label="Card front">
    <svg class="card__art" viewBox="0 0 750 428" aria-hidden="true">
      <defs>
        <linearGradient id="sheen" x1="0" y1="0" x2="1" y2="1">
          <stop offset="0" stop-color="#ffffff" stop-opacity="0"/>
          <stop offset="1" stop-color="#dcdcdc" stop-opacity="0.7"/>
        </linearGradient>
        <linearGradient id="bandFront" x1="0" y1="0" x2="1" y2="1">
          <stop offset="0" stop-color="#e8891c"/>
          <stop offset="1" stop-color="#ff9a1f"/>
        </linearGradient>
      </defs>
      <polygon points="100,428 420,108 470,108 150,428" fill="url(#sheen)" opacity="0.6"/>
      <polygon points="210,428 520,118 540,118 230,428" fill="url(#sheen)" opacity="0.8"/>
      <polygon points="380,428 700,108 740,108 420,428" fill="url(#sheen)" opacity="0.5"/>
      <polygon points="640,110 750,0 750,40 680,110" fill="url(#sheen)" opacity="0.6"/>
      <path d="M0 214 L214 0 H300 L140 160 Q100 196 55 196 L0 196 Z" fill="url(#bandFront)"/>
      <polygon points="0,0 214,0 0,214" fill="var(--navy)"/>
      <path d="M455 428 L600 283 Q642 242 690 240 L745 240 L745 230 L557 428 Z" fill="url(#bandFront)"/>
      <polygon points="750,215 750,428 537,428" fill="var(--navy)"/>
    </svg>
    <div class="brand">
      <span class="brand__main">Corvale</span>
      <span class="brand__sub">HYDRAULICS</span>
    </div>
  </section>

  <!-- Back of card -->
  <section class="card card--back" aria-label="Card back">
    <svg class="card__art" viewBox="0 0 750 428" aria-hidden="true">
      <defs>
        <linearGradient id="sheenBack" x1="0" y1="0" x2="1" y2="1">
          <stop offset="0" stop-color="#ffffff" stop-opacity="0"/>
          <stop offset="1" stop-color="#dcdcdc" stop-opacity="0.7"/>
        </linearGradient>
        <linearGradient id="bandBack" x1="0" y1="0" x2="1" y2="1">
          <stop offset="0" stop-color="#ff9f2a"/>
          <stop offset="1" stop-color="#ff8a00"/>
        </linearGradient>
      </defs>
      <polygon points="100,428 430,98 470,98 140,428" fill="url(#sheenBack)" opacity="0.6"/>
      <polygon points="210,428 560,78 575,78 225,428" fill="url(#sheenBack)" opacity="0.8"/>
      <polygon points="380,428 740,68 750,68 750,100 420,428" fill="url(#sheenBack)" opacity="0.5"/>
      <polygon points="600,110 710,0 740,0 630,110" fill="url(#sheenBack)" opacity="0.5"/>
      <path d="M240 0 H320 L390 68 Q425 115 390 160 L215 333 Q185 358 140 358 L120 358 L100 340 Z" fill="url(#bandBack)"/>
      <path d="M0 0 H245 L308 62 Q340 100 312 150 L40 428 H0 Z" fill="var(--navy)"/>
    </svg>

    <div class="brand">
      <span class="brand__main">Corvale</span>
      <span class="brand__sub">HYDRAULICS</span>
    </div>

    <div class="person">
      <p class="person__name">DANIEL REYES</p>
      <p class="person__role">Service Manager</p>
    </div>

    <ul class="contacts">
      <li class="contacts__item">
        <span>123 456 7990</span>
        <svg class="contacts__icon" viewBox="0 0 24 24" aria-label="Phone"><path fill="var(--orange)" d="M6.6 10.8a15 15 0 0 0 6.6 6.6l2.2-2.2a1 1 0 0 1 1-.25 11.4 11.4 0 0 0 3.6.6 1 1 0 0 1 1 1V20a1 1 0 0 1-1 1A17 17 0 0 1 3 4a1 1 0 0 1 1-1h3.5a1 1 0 0 1 1 1c0 1.25.2 2.45.6 3.6a1 1 0 0 1-.25 1z"/></svg>
      </li>
      <li class="contacts__item">
        <span>name@company.com</span>
        <svg class="contacts__icon" viewBox="0 0 24 24" aria-label="Email"><rect x="2" y="5" width="20" height="14" rx="1" fill="var(--orange)"/><path d="M2.5 6 L12 13 L21.5 6" fill="none" stroke="#fff" stroke-width="1.6"/></svg>
      </li>
      <li class="contacts__item">
        <span>www.company.com</span>
        <svg class="contacts__icon" viewBox="0 0 24 24" aria-label="Website"><path fill="var(--orange)" d="M5 2 L19 14 L12.5 14.5 L16 21 L13 22.5 L9.6 16 L5 20 Z"/></svg>
      </li>
      <li class="contacts__item">
        <span>123 Industrial D City, State, ZIP</span>
        <svg class="contacts__icon" viewBox="0 0 24 24" aria-label="Address"><path fill="var(--orange)" d="M12 2a7 7 0 0 0-7 7c0 5 7 13 7 13s7-8 7-13a7 7 0 0 0-7-7zm0 9.5A2.5 2.5 0 1 1 12 6.5a2.5 2.5 0 0 1 0 5z"/></svg>
      </li>
    </ul>
  </section>

</main>
</body>
</html>
```